Hip Music Management Co. BIz Card

I have a logo (attached) the back side of the card should the full logo on the entire card- that's it. The front side of the card should show the logo somewhere, keeping with the 4 different shades of blue. The front side of the card can be a white background with logo and colored typeface for all info. Pretty simple.

Target Market(s)

I manage and produce a whole bunch of major label and indie artists.

Industry/Entity Type

Management

Contact Information for Business Card

Velmora Sound House (logo)
Dale Fornwick
President
www.velmorasoundhouse.com
dale@velmorasoundhouse.com
+1 310.555.7182
418 Willow Bend Lane
Ashgrove Falls, NY 10599

Requirements
Must have
• Entire logo on back side. White background on front- unless you provide something more interesting.
Nice to have
• On the front of the card if you choose a white backgound, if possible take my logo without the blue background (over white) that would be cool.

```html
<!DOCTYPE html>
<html lang="en">
<head>
<meta charset="utf-8">
<title>Velmora Sound House — Business Card</title>
<link rel="stylesheet" href="https://fonts.googleapis.com/css2?family=Open+Sans:wght@400;600&display=swap">
<style>
  :root {
    --page-bg: #e9ebf0;
    --navy: #1f1f5c;
    --navy-deep: #1a1a52;
    --teal-light: #4a90b0;
    --teal-mid: #2f6d98;
    --blue-edge: #27467e;
    --brand-blue: #7dcdf0;
    --ink-light: #e6eef6;
    --ink-soft: #c9d8e6;
  }
  * { box-sizing: border-box; margin: 0; padding: 0; }
  html, body { width: 1200px; height: 1000px; overflow: hidden; }
  body {
    background: var(--page-bg);
    font-family: "Open Sans", Arial, sans-serif;
    position: relative;
  }
  .card {
    position: absolute;
    width: 620px;
    height: 345px;
    box-shadow: 0 6px 18px rgba(20, 20, 50, 0.25);
    overflow: hidden;
  }
  /* Front side */
  .card--front {
    left: 170px;
    top: 110px;
    background: var(--navy);
    display: flex;
  }
  .card--front .brand-panel {
    width: 46%;
    display: flex;
    align-items: center;
    padding-left: 36px;
  }
  .card--front .contact-panel {
    width: 54%;
    position: relative;
    background: linear-gradient(180deg, var(--blue-edge) 0%, var(--teal-mid) 35%, var(--teal-light) 65%, var(--blue-edge) 100%);
    box-shadow: inset 22px 0 22px -10px rgba(10, 15, 50, 0.55);
    padding: 40px 34px 0 0;
    text-align: right;
    color: var(--ink-light);
  }
  .brand-name {
    color: var(--brand-blue);
    font-weight: 600;
    line-height: 1.05;
    letter-spacing: 0.5px;
  }
  .card--front .brand-name { font-size: 30px; }
  .person-name { font-size: 27px; font-weight: 400; }
  .person-title { font-size: 14px; color: var(--ink-soft); margin-top: 2px; }
  .address { font-size: 14px; line-height: 1.45; margin-top: 34px; color: var(--ink-soft); }
  .phone { font-size: 14px; margin-top: 22px; color: var(--ink-soft); }
  .online { font-size: 14px; line-height: 1.45; margin-top: 22px; color: var(--ink-soft); }

  /* Back side */
  .card--back {
    left: 410px;
    top: 520px;
    width: 600px;
    height: 340px;
    background: var(--navy);
  }
  .card--back .brand-area {
    height: 212px;
    display: flex;
    align-items: flex-end;
    justify-content: center;
    padding-bottom: 22px;
  }
  .card--back .brand-name { font-size: 46px; }
  .card--back .glow-band {
    height: 128px;
    background:
      radial-gradient(ellipse 60% 90% at 50% 50%, rgba(74, 150, 180, 0.95) 0%, rgba(47, 109, 152, 0.8) 45%, rgba(31, 31, 92, 0.9) 100%);
    box-shadow: inset 0 12px 14px -8px rgba(10, 10, 40, 0.6);
  }
</style>
</head>
<body>
  <section class="card card--front" aria-label="Business card front">
    <div class="brand-panel">
      <p class="brand-name">Velmora<br>Sound House</p>
    </div>
    <div class="contact-panel">
      <p class="person-name">Dale Fornwick</p>
      <p class="person-title">President</p>
      <p class="address">Velmora Sound House<br>418 Willow Bend Lane<br>Ashgrove Falls, NY 10599</p>
      <p class="phone">+1 310.555.7182</p>
      <p class="online">dale@velmorasoundhouse.com<br>www.velmorasoundhouse.com</p>
    </div>
  </section>

  <section class="card card--back" aria-label="Business card back">
    <div class="brand-area">
      <p class="brand-name">Velmora Sound House</p>
    </div>
    <div class="glow-band"></div>
  </section>
</body>
</html>
```